New concept for existing event brand

I have this current brand - www.hollow-pulse.com I have attached an example of a credible event on 23rd December and then a more fun brunch event.

I require a new flyer for a new concept - Velvet Recess - (there is no logo yet) it is at a venue which has ball pits, table tennis, beer pong, arcades etc

I am looking for an artwork which portrays a fun event but also retains the cooler brand identify

One idea was having the images in polaroid frames

Velvet Recess

Saturday 18th February 2023

Venue to be announced • 3pm-9pm

2 giant ball pits
Beer pong
Ping Pong
Boxing machines
Dance Machine
Air Hockey
Pool
Giant board games
Giant Clink Row
Photo Booth
Spin The Wheel
Table Football
Retro Arcade Games
Pinball

Food
Pizzas
Brim Curls
Popcorn
Candy Floss

Cocktails
Alcoholic Glace Rockets
Beer Towers
Spirits & Mixers

```html
<!DOCTYPE html>
<html lang="en">
<head>
<meta charset="utf-8">
<title>Velvet Recess</title>
<link rel="stylesheet" href="https://fonts.googleapis.com/css2?family=Russo+One&family=Oswald:wght@500;600&family=Montserrat:wght@400;500&family=Poppins:wght@500;600;700&display=swap">
<style>
:root{
  --night:#140a1c;
  --plum:#2a1238;
  --indigo:#1d1660;
  --glow-blue:#3b3fd8;
  --hot-pink:#ff1aa6;
  --white:#ffffff;
  --soft-white:#ece8f2;
}
*{margin:0;padding:0;box-sizing:border-box}
html,body{width:800px;height:1200px;overflow:hidden;background:var(--night)}
.flyer{
  position:relative;width:800px;height:1200px;overflow:hidden;
  background:
    radial-gradient(ellipse 60% 30% at 50% 55%, rgba(70,50,220,.55), transparent 70%),
    radial-gradient(ellipse 80% 25% at 50% 15%, rgba(120,30,110,.5), transparent 70%),
    linear-gradient(180deg,#2a1233 0%,#24133d 30%,#1b1a6a 55%,#0e0a18 80%,#0b0812 100%);
  font-family:"Montserrat",sans-serif;color:var(--white);text-align:center;
}
.backdrop-glow{
  position:absolute;left:0;right:0;top:300px;height:520px;
  background:radial-gradient(ellipse 50% 50% at 50% 50%, rgba(90,80,255,.35), transparent 75%);
}
.crowd{
  position:absolute;left:0;right:0;bottom:0;height:260px;
  background:linear-gradient(180deg,transparent,rgba(60,20,90,.45) 40%,rgba(10,6,16,.9));
}
.event-title{
  position:absolute;top:58px;left:0;right:0;
  font-family:"Russo One",sans-serif;font-size:72px;letter-spacing:1px;font-weight:400;
  color:var(--soft-white);
}
.event-date{
  position:absolute;top:138px;left:0;right:0;
  font-family:"Oswald",sans-serif;font-weight:600;font-size:54px;color:var(--hot-pink);letter-spacing:.5px;
}
.event-date .day{color:var(--white)}
.event-date sup{font-size:26px;vertical-align:22px}
.event-venue{
  position:absolute;top:210px;left:0;right:0;
  font-weight:500;font-size:28px;letter-spacing:1.5px;
}
.event-time{
  position:absolute;top:248px;left:0;right:0;
  font-family:"Oswald",sans-serif;font-weight:600;font-size:54px;
}
.polaroid{
  position:absolute;border:8px solid var(--hot-pink);
  box-shadow:0 6px 18px rgba(0,0,0,.5);
}
.polaroid--ballpit{left:130px;top:345px;width:270px;height:205px;transform:rotate(-8deg);
  background:linear-gradient(135deg,#e9ddf3,#b58ad8 50%,#5b2a8a)}
.polaroid--arcade{left:412px;top:340px;width:260px;height:200px;transform:rotate(5deg);
  background:linear-gradient(135deg,#3b6a3a,#c98a6e 45%,#4a62a0)}
.polaroid--beerpong{left:140px;top:540px;width:265px;height:225px;transform:rotate(-8deg);
  background:linear-gradient(135deg,#3a2c6a,#7a4c7a 50%,#c83040)}
.polaroid--friends{left:410px;top:535px;width:260px;height:225px;transform:rotate(3deg);
  background:linear-gradient(135deg,#d8d2cc,#9a8272 50%,#2f6fc0)}
.pill{
  position:absolute;background:var(--hot-pink);color:var(--white);
  font-family:"Poppins",sans-serif;font-weight:600;font-size:24px;
  border-radius:8px;height:38px;line-height:38px;
}
.pill--games{left:306px;top:808px;width:174px}
.pill--food{left:185px;top:951px;width:176px}
.pill--cocktails{left:490px;top:954px;width:176px}
.list{
  position:absolute;font-size:15.5px;letter-spacing:.3px;line-height:23px;color:var(--soft-white);
}
.list .sep{color:var(--hot-pink);padding:0 7px}
.list--games{top:858px;left:0;right:0}
.list--food{top:1000px;left:120px;width:290px;line-height:20px}
.list--cocktails{top:1004px;left:415px;width:330px;line-height:20px}
.brand-name{
  position:absolute;top:1060px;left:0;right:0;
  font-family:"Poppins",sans-serif;font-weight:700;font-size:50px;letter-spacing:1px;color:var(--soft-white);
}
.brand-url{
  position:absolute;top:1128px;left:0;right:0;
  font-family:"Poppins",sans-serif;font-weight:600;font-size:22px;letter-spacing:.5px;
}
.brand-url .accent{color:var(--hot-pink)}
</style>
</head>
<body>
<main class="flyer">
  <div class="backdrop-glow" role="img" aria-label="Neon light backdrop behind the photos"></div>
  <div class="crowd" role="img" aria-label="Silhouetted party crowd with raised hands"></div>

  <h1 class="event-title">VELVET RECESS</h1>
  <p class="event-date">SATURDAY <span class="day">18<sup>TH</sup></span> FEBRUARY 2023</p>
  <p class="event-venue">VENUE TO BE ANNOUNCED</p>
  <p class="event-time">3PM-9PM</p>

  <div class="polaroid polaroid--ballpit" role="img" aria-label="Photo of white balloons in a ball pit under purple light"></div>
  <div class="polaroid polaroid--arcade" role="img" aria-label="Photo of guests playing a dance arcade machine"></div>
  <div class="polaroid polaroid--beerpong" role="img" aria-label="Photo of a group playing beer pong at a red table"></div>
  <div class="polaroid polaroid--friends" role="img" aria-label="Photo of friends laughing in a ball pit"></div>

  <div class="pill pill--games">GAMES</div>
  <p class="list list--games">
    2 GIANT BALL PITS<span class="sep">|</span>BEER PONG<span class="sep">|</span>PING PONG<span class="sep">|</span>BOXING MACHINES<span class="sep">|</span>DANCE MACHINE<br>
    AIR HOCKEY<span class="sep">|</span>POOL<span class="sep">|</span>GIANT BOARD GAMES<span class="sep">|</span>GIANT CLINK ROW<span class="sep">|</span>PINBALL<br>
    PHOTO BOOTH<span class="sep">|</span>RETRO ARCADE GAMES<span class="sep">|</span>TABLE FOOTBALL<span class="sep">|</span>SPIN THE WHEEL
  </p>

  <div class="pill pill--food">FOOD</div>
  <p class="list list--food">
    PIZZAS<span class="sep">|</span>POPCORN<br>
    BRIM CURLS<span class="sep">|</span>CANDY FLOSS
  </p>

  <div class="pill pill--cocktails">COCKTAILS</div>
  <p class="list list--cocktails">
    BEER TOWERS<span class="sep">|</span>SPIRITS &amp; MIXERS<br>
    ALCOHOLIC GLACE ROCKETS
  </p>

  <p class="brand-name">HOLLOW PULSE</p>
  <p class="brand-url">www.<span class="accent">hollow-pulse</span>.com</p>
</main>
</body>
</html>
```